Emergency Flip Chart Edit/ Upgrade
Sexify my flipchart please!!!
Emergency Flip Chart Edit/ Upgrade - Emergency Services
Creative Brief
I have an emergency flip chart that has been drafted, but the graphic designer did not do what I asked, so I need a redesign of it. I'd like the front cover to look similar to the front header of tinyshopgrowthideas.com.au - cartoonish - but the cartoon to resemble myself (will enclose photos). The rest of the flip chart pages to be slightly more polished.
Emergency Services
Corporate, although with the cool/ creative edge.
Redesign of flip chart - ready to be sent to the printers with all the relevant information on page thickness etc that the printer will require.
Hazardwise Hazardwise
Excellent! Love it. Ready to finalise the project so thank you for all your hard work. Just a few small things. Could you take off my photo and the circle behind it. Change Frst Aid to First Aid Take out 'be safe not sorry' and replace with enquiries 0412 736 908. How did you go with the other pages, are they needed to be changed? My email address is milliekate@hazardwiseadvisory.com.au if you'd like to send them through.
Also, please have a look at the other pages on the flip chart, including the calander that sits at the bottom of the flip chart and make amendments to tie in the theme - this needs only to be very minor changes.
I am now getting a illustrated cartoon of myself - so this will replace the photo. It will be ready in 5 days - this will need to be added once I receive it. It's hard to see the green in the logo - move logo. Under the title 'emergency procedures' under the crane include 'emergencies 000' which is the emergency number in Australia to call. Remove www.hazardwise.com Remove 'be safe not sorry' Replace all writing down below to include - arranged to look nice: PO Box 57 Keldara NSW 2384 info@hazardwiseadvisory.com.au www.hazardwiseadvisory.com.au - safety management systems - accredited auditing - legislative gap analysis - asbestos audits - safety culture TRAINING - first aid - HSR 5 day committee course - committees - fire warden/ evac drills - manager/ supervisor responsibilities - legislative due diligence - manual handling - ergonomics - risk management - investigations - armed hold ups - asbestos awareness/ demolition - cert IV workplace health & safety - responsible service alcohol - responsible gaming services Find Hazardwise on Facebook, Linkedin, Twitter, Youtube, Itunes (include the logos of each)
Pendrake Pendrake

```html
<!DOCTYPE html>
<html lang="en">
<head>
<meta charset="utf-8">
<title>Emergency Procedures – Hazardwise</title>
<link rel="stylesheet" href="https://fonts.googleapis.com/css2?family=Oswald:wght@600;700&family=Open+Sans:ital,wght@0,400;0,700;0,800;1,700&display=swap">
<style>
  :root {
    --green-dark: #1f6a2a;
    --green-mid: #2b8a34;
    --green-light: #3a9e3f;
    --orange: #f39a12;
    --orange-light: #fbc630;
    --orange-deep: #e97f0c;
    --yellow-title: #ffd21f;
    --silver-top: #ffffff;
    --silver-bottom: #9a9a9a;
    --footer: #3a3a3a;
    --white: #ffffff;
    --cream: #fff6cc;
  }
  * { box-sizing: border-box; margin: 0; padding: 0; }
  html, body { width: 1200px; height: 722px; overflow: hidden; background: var(--white); }
  .cover {
    position: relative;
    width: 1200px;
    height: 722px;
    overflow: hidden;
    font-family: "Open Sans", Arial, sans-serif;
  }
  .cover__sky {
    position: absolute; left: 0; top: 0; width: 1200px; height: 468px;
    background:
      repeating-linear-gradient(90deg,
        rgba(255,255,255,0.00) 0 70px,
        rgba(255,255,255,0.06) 70px 150px,
        rgba(0,0,0,0.05) 150px 200px),
      linear-gradient(180deg, var(--green-mid), var(--green-dark));
  }
  .crane-art {
    position: absolute; left: 70px; top: 78px; width: 330px; height: 360px;
    background: linear-gradient(160deg, rgba(247,160,30,0.85), rgba(233,127,12,0.55));
    border-radius: 6px;
  }
  .brand {
    position: absolute; right: 36px; top: 26px; text-align: right;
  }
  .brand__row { display: flex; align-items: center; justify-content: flex-end; gap: 14px; }
  .brand__dot { width: 40px; height: 40px; border-radius: 50%; background: var(--orange); }
  .brand__name {
    font-family: "Open Sans", Arial, sans-serif; font-weight: 800;
    font-size: 64px; line-height: 1; color: var(--orange); letter-spacing: -1px;
  }
  .brand__tagline {
    margin-top: 4px; font-size: 22px; letter-spacing: 3px; color: var(--white);
  }
  .portrait {
    position: absolute; left: 848px; top: 152px; width: 236px; height: 236px;
    border-radius: 50%; border: 8px solid var(--white);
    box-shadow: 0 0 0 6px var(--orange);
    background: radial-gradient(circle at 50% 40%, #d9b7a0, #8a6a5a);
  }
  .motto {
    position: absolute; left: 826px; top: 402px; width: 290px; text-align: center;
    font-style: italic; font-weight: 700; font-size: 28px; color: var(--white);
  }
  .title {
    position: absolute; left: 168px; top: 206px;
    font-family: "Oswald", Impact, sans-serif; font-weight: 700; text-transform: uppercase;
    line-height: 0.98;
  }
  .title__line { display: block; text-shadow: 3px 4px 4px rgba(0,0,0,0.45); }
  .title__line--first {
    font-size: 90px; letter-spacing: 1px;
    color: #d8d8d8;
    background: linear-gradient(180deg, var(--silver-top), var(--silver-bottom));
    -webkit-background-clip: text; background-clip: text; -webkit-text-fill-color: transparent;
    filter: drop-shadow(3px 4px 3px rgba(0,0,0,0.45));
    text-shadow: none;
  }
  .title__line--second { font-size: 104px; color: var(--yellow-title); margin-left: 12px; }
  .cover__band {
    position: absolute; left: 0; top: 468px; width: 1200px; height: 222px;
    background: linear-gradient(180deg, var(--orange-light) 0%, var(--orange) 45%, var(--orange-deep) 100%);
    border-top: 4px solid #fde37a;
  }
  .training { position: absolute; left: 112px; top: 22px; width: 840px; color: var(--white); }
  .training__heading { display: flex; align-items: center; gap: 12px; font-size: 28px; font-weight: 700; }
  .training__bullet { width: 22px; height: 22px; background: var(--green-mid); border: 2px solid var(--white); }
  .training__sub { margin: 12px 0 4px 42px; font-size: 17px; font-weight: 700; color: var(--cream); }
  .training__text { margin-left: 42px; font-size: 15px; line-height: 1.4; }
  .cover__footer {
    position: absolute; left: 0; top: 690px; width: 1200px; height: 32px;
    background: var(--footer); color: var(--white);
    font-size: 16px; font-weight: 700; text-align: right; padding: 5px 36px 0 0;
  }
</style>
</head>
<body>
<main class="cover">
  <div class="cover__sky"></div>
  <div class="crane-art" role="img" aria-label="Illustration of an orange construction tower crane"></div>

  <div class="brand">
    <div class="brand__row">
      <span class="brand__dot"></span>
      <span class="brand__name">Hazardwise</span>
    </div>
    <p class="brand__tagline">safety consultancy</p>
  </div>

  <div class="portrait" role="img" aria-label="Portrait photo of the consultant in a circular frame"></div>
  <p class="motto">“Be safe, not sorry “</p>

  <h1 class="title">
    <span class="title__line title__line--first">Emergency</span>
    <span class="title__line title__line--second">Procedures</span>
  </h1>

  <section class="cover__band">
    <div class="training">
      <h2 class="training__heading"><span class="training__bullet"></span>listing of training</h2>
      <h3 class="training__sub">Introduction</h3>
      <p class="training__text">A training program has to be developed to meet the individual needs of the athlete and take into consideration many factors: gender, age, strengths, weaknesses, objectives, training facilities etc. As all athletes have different needs, a single program suitable for all athletes is not possible.</p>
    </div>
  </section>

  <footer class="cover__footer">www.hazardwise.com</footer>
</main>
</body>
</html>
```